Scratch Card for Student Promotion

I'm wanting a series of 'Scratch Cards' designed for behaviour rewards for students. I need the following designed:
- Front of scratch card - Showing the logo, VALOR values and sections where the scratch off material is put.
- Instructions for the cards - Find three matching symbols to win a prize.
These should show 6 scratch sections in a 3x2 arrangement.
- Back of card - With sections for the:
- Teacher name (person allocating the reward)
- Student Name, House and Form Class - To be used for a second change draw.
- 8 alternative fronts, that show the design for when the 'Scratch' section has been scratched off.
- These should show six boxes (3x2) and have:
- 2 designs for not winning that show 3 'Second Change Draw' symbols.
- 6 designs for winning a variety pf prizes including:
- Skip the line at the tuckshop
- Handball
- Yoyo
- Stress ball
- Playing cards
- $5 Tuckshop Voucher
I've included
- the Kestal VALOR (our values Structure) logo
- The print outline required for the project
- Our VALOR matrix and Kestal Path document to assist with styling and additional wording for the project.

```html
<!DOCTYPE html>
<html lang="en">
<head>
<meta charset="utf-8">
<title>Kestal VALOR Scratch and Win Card</title>
<link href="https://fonts.googleapis.com/css2?family=Anton&family=Bebas+Neue&family=Poppins:wght@400;600&display=swap" rel="stylesheet">
<style>
  :root {
    --stage: #878787;
    --card-blue: #3e4095;
    --panel-blue: #3d3f93;
    --shade: rgba(20, 18, 50, 0.55);
    --gold: #f3e47f;
    --white: #ffffff;
    --footer: #241c35;
    --silver-light: #e2e2e6;
    --silver-dark: #8a8a8e;
  }
  * { box-sizing: border-box; margin: 0; padding: 0; }
  html, body { width: 1015px; height: 1200px; overflow: hidden; }
  body { background: var(--stage); position: relative; font-family: "Poppins", sans-serif; }

  .card {
    position: absolute; width: 677px; height: 414px;
    background: var(--card-blue); overflow: hidden;
    box-shadow: 0 6px 18px rgba(0,0,0,0.25);
  }
  .card--front { left: 152px; top: 133px; }
  .card--back { left: 147px; top: 656px; }

  .brand-panel {
    position: absolute; left: 0; top: 0; width: 193px; height: 139px;
    background: var(--panel-blue);
    box-shadow: 0 14px 18px var(--shade);
    display: flex; align-items: center; justify-content: center; gap: 8px;
  }
  .brand-dot { width: 18px; height: 18px; border-radius: 50%; background: var(--gold); flex: none; }
  .brand-name {
    font-family: "Bebas Neue", sans-serif; color: var(--gold);
    font-size: 30px; line-height: 1; letter-spacing: 1px; white-space: nowrap;
  }
  .chevron { position: absolute; left: 190px; top: 0; width: 36px; height: 139px; }

  .title-scratch {
    position: absolute; left: 243px; top: 8px;
    font-family: "Bebas Neue", sans-serif; color: var(--gold);
    font-size: 80px; line-height: 1; letter-spacing: -2px;
  }
  .title-and {
    position: absolute; left: 243px; top: 84px; width: 212px;
    display: flex; align-items: center; justify-content: space-between;
    font-family: "Bebas Neue", sans-serif; color: var(--gold);
    font-size: 44px; line-height: 1;
  }
  .title-and .rule { display: block; width: 66px; height: 5px; background: var(--gold); }
  .title-win {
    position: absolute; left: 464px; top: 6px;
    font-family: "Anton", sans-serif; color: var(--gold);
    font-size: 112px; line-height: 1; letter-spacing: -3px;
  }

  .values-heading {
    position: absolute; left: 18px; top: 165px; width: 231px;
    border-top: 4px solid var(--gold); border-bottom: 4px solid var(--gold);
    font-family: "Bebas Neue", sans-serif; color: var(--gold);
    font-size: 40px; line-height: 40px; letter-spacing: 1px; text-align: center;
  }
  .values-list { position: absolute; left: 32px; top: 226px; width: 230px; list-style: none; }
  .values-list li {
    font-size: 10px; font-weight: 600; color: var(--white);
    line-height: 13.4px; letter-spacing: 0.3px; display: flex; white-space: nowrap;
  }
  .values-list .initial { color: var(--gold); width: 15px; }

  .instructions {
    position: absolute; left: 36px; top: 330px;
    font-family: "Bebas Neue", sans-serif; color: var(--gold);
    font-size: 28px; line-height: 25px;
  }

  .scratch-frame {
    position: absolute; left: 272px; top: 161px; width: 390px; height: 233px;
    border: 5px solid var(--gold);
  }
  .scratch-box {
    position: absolute; width: 115px; height: 97px;
    background: linear-gradient(125deg, var(--silver-dark) 0%, var(--silver-light) 30%, var(--silver-dark) 58%, #b9b9bd 80%, var(--silver-dark) 100%);
  }
  .scratch-box::after {
    content: ""; position: absolute; left: 50%; top: 50%;
    width: 14px; height: 14px; margin: -7px 0 0 -7px;
    border-radius: 50%; background: #4b4b50;
  }

  .chance-heading {
    position: absolute; left: 32px; top: 186px;
    font-family: "Bebas Neue", sans-serif; font-size: 36px; line-height: 38px;
    letter-spacing: -0.3px; white-space: nowrap;
    background: linear-gradient(90deg, #e4e4ea, #9e9eaa);
    -webkit-background-clip: text; background-clip: text; color: transparent;
  }
  .chance-rule {
    position: absolute; left: 80px; width: 134px; height: 2px;
    background: linear-gradient(90deg, transparent, #d9d9e0, transparent);
  }
  .prize-copy {
    position: absolute; left: 33px; top: 240px; width: 282px;
    color: var(--white); font-size: 17px; line-height: 21px;
  }

  .field-label {
    position: absolute; font-family: "Bebas Neue", sans-serif;
    color: var(--gold); font-size: 15px; line-height: 1;
  }
  .field-box { position: absolute; background: var(--white); border-radius: 4px; height: 32px; }

  .footer-bar {
    position: absolute; left: 0; bottom: 0; width: 100%; height: 54px;
    background: var(--footer);
    display: flex; align-items: center; justify-content: space-between;
    padding: 0 15px 0 33px;
  }
  .footer-note { color: var(--white); font-size: 11.5px; white-space: nowrap; }
  .footer-motto {
    font-family: "Bebas Neue", sans-serif; color: var(--white);
    font-size: 36px; line-height: 1; white-space: nowrap;
  }
</style>
</head>
<body>

<section class="card card--front" aria-label="Scratch card front">
  <div class="brand-panel">
    <span class="brand-dot"></span>
    <span class="brand-name">Kestal VALOR</span>
  </div>
  <svg class="chevron" viewBox="0 0 36 139" aria-hidden="true">
    <defs>
      <linearGradient id="chev-a" x1="0" x2="1"><stop offset="0" stop-color="#f3e47f"/><stop offset="1" stop-color="#b8a84e"/></linearGradient>
    </defs>
    <polygon points="0,0 14,0 36,69 14,139 0,139 22,69" fill="url(#chev-a)"/>
  </svg>
  <div class="title-scratch">SCRATCH</div>
  <div class="title-and"><span class="rule"></span>AND<span class="rule"></span></div>
  <div class="title-win">WIN!</div>

  <h2 class="values-heading">VALOR VALUES</h2>
  <ul class="values-list">
    <li><span class="initial">V</span>Vigour and Perseverance</li>
    <li><span class="initial">A</span>Accountability and Respect</li>
    <li><span class="initial">L</span>Loyalty and Integrity</li>
    <li><span class="initial">O</span>Openness to Diversity</li>
    <li><span class="initial">R</span>Rising through Engagement</li>
  </ul>
  <p class="instructions">FIND THE MATCHING<br>SYMBOLS TO WIN!</p>

  <div class="scratch-frame"></div>
  <div class="scratch-box" style="left:287px;top:176px"></div>
  <div class="scratch-box" style="left:409px;top:176px"></div>
  <div class="scratch-box" style="left:530px;top:176px"></div>
  <div class="scratch-box" style="left:287px;top:279px"></div>
  <div class="scratch-box" style="left:409px;top:279px"></div>
  <div class="scratch-box" style="left:530px;top:279px"></div>
</section>

<section class="card card--back" aria-label="Scratch card back">
  <div class="brand-panel">
    <span class="brand-dot"></span>
    <span class="brand-name">Kestal VALOR</span>
  </div>
  <svg class="chevron" viewBox="0 0 36 139" aria-hidden="true">
    <defs>
      <linearGradient id="chev-b" x1="0" x2="1"><stop offset="0" stop-color="#f3e47f"/><stop offset="1" stop-color="#b8a84e"/></linearGradient>
    </defs>
    <polygon points="0,0 14,0 36,69 14,139 0,139 22,69" fill="url(#chev-b)"/>
  </svg>
  <div class="title-scratch">SCRATCH</div>
  <div class="title-and"><span class="rule"></span>AND<span class="rule"></span></div>
  <div class="title-win">WIN!</div>

  <span class="chance-rule" style="top:182px"></span>
  <h2 class="chance-heading">GET A CHANCE TO WIN</h2>
  <span class="chance-rule" style="top:228px"></span>
  <p class="prize-copy">Don’t miss your chance to win free skip the line at the tuckshop, handball, yoyo, stress ball, playing cards &amp; $5 tuckshop voucher!</p>

  <span class="field-label" style="left:382px;top:176px">TEACHER</span>
  <div class="field-box" style="left:381px;top:192px;width:256px"></div>
  <span class="field-label" style="left:382px;top:229px">STUDENT</span>
  <div class="field-box" style="left:381px;top:245px;width:256px"></div>
  <span class="field-label" style="left:382px;top:284px">HOUSE</span>
  <div class="field-box" style="left:381px;top:300px;width:102px"></div>
  <span class="field-label" style="left:536px;top:284px">FORM</span>
  <div class="field-box" style="left:535px;top:300px;width:102px"></div>

  <div class="footer-bar">
    <span class="footer-note">Note: Submitted names would be used in the second chance draw</span>
    <span class="footer-motto">THE KESTAL PATH</span>
  </div>
</section>

</body>
</html>
```